TK Drafting

Simple Design - Logo is done (from this site). Logo on one side - Back Side an image or outline of a house blue print - My name, phone, email, website url. Prefer the traditional Architectural style of letters -

Target Market(s)

Customers who need a floor plan redesigned for renovations or realtors who want a floor plan for marketing their listings

Industry/Entity Type

Architecture

Contact Information for Business Card

Colin Varga - Name
318-542-6604 - Phone
tkdraftingco@mailvane.com
www.tkdraftingco.net

Font styles to use
Other font styles liked:
• Architecture writing -

Colors
0555a3
3276b5
85acd3

Requirements
Must have
• Logo that is attached. I like an indigo blue color for the background or a royal blue - gray logo OR - white and clean with the logo on one side and the same color gray lettering on the other side
Nice to have
• some sort of image that shows a residential blue print. It may not be possible on this small of a card though.
Should not have
• Nothing cartoonish.

```html
<!DOCTYPE html>
<html lang="en">
<head>
<meta charset="utf-8">
<title>TK Drafting — Business Card</title>
<link href="https://fonts.googleapis.com/css2?family=Rubik:wght@400;500&display=swap" rel="stylesheet">
<style>
  :root {
    --page-bg: #c6c6c8;
    --card-blue: #233f87;
    --card-white: #ffffff;
    --logo-gray: #a9acb7;
    --ink-gray: #56575c;
    --plan-tint-a: #f6f6f8;
    --plan-tint-b: #eeeff2;
    --divider: #8c8d92;
  }
  * { box-sizing: border-box; margin: 0; padding: 0; }
  html, body { width: 1200px; height: 900px; overflow: hidden; }
  body {
    background: var(--page-bg);
    font-family: "Rubik", sans-serif;
    position: relative;
  }
  .card {
    position: absolute;
    left: 250px;
    width: 700px;
    height: 400px;
    box-shadow: 0 6px 16px rgba(0,0,0,0.18);
  }
  .card-front {
    top: 35px;
    background: var(--card-blue);
    display: flex;
    align-items: center;
    justify-content: center;
  }
  .brand-name {
    display: flex;
    align-items: center;
    gap: 16px;
    color: var(--logo-gray);
    font-size: 52px;
    font-weight: 500;
    letter-spacing: 2px;
  }
  .brand-mark {
    width: 22px;
    height: 22px;
    background: var(--logo-gray);
  }
  .card-back {
    top: 465px;
    background: var(--card-white);
    overflow: hidden;
  }
  .floor-plan-backdrop {
    position: absolute;
    inset: 0;
    background: linear-gradient(135deg, var(--plan-tint-a), var(--plan-tint-b) 55%, var(--plan-tint-a));
  }
  .contact-block {
    position: absolute;
    left: 0; right: 0;
    top: 150px;
    display: flex;
    align-items: center;
    justify-content: center;
    gap: 26px;
  }
  .holder-name {
    color: var(--ink-gray);
    font-size: 30px;
    font-weight: 500;
    letter-spacing: 0.5px;
    text-transform: uppercase;
  }
  .divider {
    width: 1.5px;
    height: 88px;
    background: var(--divider);
  }
  .contact-list {
    list-style: none;
    color: var(--ink-gray);
    font-size: 19px;
    line-height: 30px;
    letter-spacing: 0.6px;
  }
  .contact-list li { display: flex; align-items: center; gap: 10px; }
  .contact-list svg { width: 18px; height: 18px; flex: none; }
</style>
</head>
<body>
  <section class="card card-front" aria-label="Business card front">
    <div class="brand-name"><span class="brand-mark"></span>TK Drafting</div>
  </section>

  <section class="card card-back" aria-label="Business card back">
    <div class="floor-plan-backdrop" role="img" aria-label="Faint residential floor plan blueprint with labelled rooms"></div>
    <div class="contact-block">
      <h1 class="holder-name">Colin Varga</h1>
      <div class="divider"></div>
      <ul class="contact-list">
        <li>
          <svg viewBox="0 0 24 24" fill="none" stroke="currentColor" stroke-width="2" stroke-linejoin="round"><path d="M5 3h4l2 5-2.5 1.5a11 11 0 0 0 6 6L16 13l5 2v4a2 2 0 0 1-2 2A16 16 0 0 1 3 5a2 2 0 0 1 2-2z"/></svg>
          318-542-6604
        </li>
        <li>
          <svg viewBox="0 0 24 24" fill="none" stroke="currentColor" stroke-width="2"><rect x="3" y="5" width="18" height="14"/><path d="M3 5l9 8 9-8M3 19l7-7M21 19l-7-7"/></svg>
          tkdraftingco@mailvane.com
        </li>
        <li>
          <svg viewBox="0 0 24 24" fill="none" stroke="currentColor" stroke-width="1.8"><circle cx="12" cy="12" r="9"/><ellipse cx="12" cy="12" rx="4" ry="9"/><path d="M3 12h18M5 7h14M5 17h14"/></svg>
          www.tkdraftingco.net
        </li>
      </ul>
    </div>
  </section>
</body>
</html>
```